Creative, fresh business card design for Orrin Linings

We need a fresh, creative business card design for Orrin Linings. We are the manufacturer of Orrin Linings in Australia. Wall panels are 2400 x 1200mm panels made from MDF and feature 3D patterns on the face of the panel. The colours to be used are green, silver/grey and white RGB
Red 187
Green 207
Blue 65.

An idea is to possibly use a watermark of one of our designs as a background (like on the "Ferns" design on the left hand side of page 2 of our brochure).

Target Market(s)

Interior designers, architects, builders and home renovators

Industry/Entity Type

Business

Contact Information for Business Card

Details to go on the card are:
Our logo (attached),
Slogan: "Decorative panels for interiors and exteriors",
Contact name,
Position,
Mobile phone number,
Business address,
Business phone,
Business fax,
Website and
Email address.

I have attached a few images of our panels and our brochure for reference.

The colours of the business card should feature our logo colours which are: RGB
Red 187
Green 207
Blue 65

Requirements
Must have
• Very modern fonts and design. Some of the designs shown especially the "Weave" design which is a popular design.
Nice to have
• Creative but simple design. Very contemporary.
Should not have
• Anything ornate or old fashioned.

```html
<!DOCTYPE html>
<html lang="en">
<head>
<meta charset="utf-8">
<title>Orrin Linings – Business Card</title>
<link href="https://fonts.googleapis.com/css2?family=Lato:wght@400;700&display=swap" rel="stylesheet">
<style>
  :root {
    --brand-green: rgb(187, 207, 65);
    --brand-grey: #8c8d90;
    --card-white: #ffffff;
    --pattern-light: #f4f4f4;
    --pattern-mid: #dcdcdc;
    --slogan-grey: #77787b;
    --stage: #e9e9ea;
  }
  * { box-sizing: border-box; margin: 0; padding: 0; }
  html, body { width: 1200px; height: 900px; overflow: hidden; }
  body {
    background: var(--stage);
    font-family: "Lato", sans-serif;
    position: relative;
  }
  .card {
    position: absolute;
    top: 301px;
    width: 515px;
    height: 297px;
    background: var(--card-white);
    box-shadow: 0 2px 8px rgba(0,0,0,0.18);
  }
  .card--front { left: 70px; }
  .card--back { left: 615px; }

  .panel-pattern {
    position: absolute;
    background:
      linear-gradient(135deg, var(--pattern-light) 0%, var(--pattern-mid) 50%, var(--pattern-light) 100%);
  }
  .card--front .panel-pattern { left: 22px; top: 20px; width: 471px; height: 257px; }

  .brand {
    position: absolute;
    display: flex;
    align-items: center;
    gap: 10px;
  }
  .brand__square {
    width: 34px;
    height: 34px;
    background: var(--brand-green);
    flex: none;
  }
  .brand__name {
    font-family: "Lato", sans-serif;
    font-weight: 700;
    color: var(--brand-grey);
    white-space: nowrap;
  }
  .card--front .brand { left: 50%; top: 50%; transform: translate(-50%, -50%); }
  .card--front .brand__name { font-size: 30px; }

  .contact-person {
    position: absolute;
    left: 22px; top: 20px; width: 164px; height: 135px;
    background: var(--brand-grey);
    color: var(--card-white);
    padding: 34px 0 0 20px;
    font-size: 13px;
    line-height: 18px;
  }
  .contact-person__name { font-weight: 700; }
  .contact-person__mobile { margin-top: 16px; }
  .contact-person__mobile b { font-weight: 700; }

  .card--back .panel-pattern { left: 192px; top: 20px; width: 301px; height: 135px; }

  .card--back .brand {
    left: 22px; top: 160px; width: 164px; height: 98px;
    justify-content: center;
    gap: 8px;
  }
  .card--back .brand__square { width: 22px; height: 22px; }
  .card--back .brand__name { font-size: 18px; }

  .contact-business {
    position: absolute;
    left: 192px; top: 160px; width: 301px; height: 98px;
    background: var(--brand-green);
    color: var(--card-white);
    padding: 13px 0 0 12px;
    font-size: 13px;
    line-height: 19px;
  }
  .contact-business b, .contact-business .web { font-weight: 700; }

  .slogan {
    position: absolute;
    left: 22px; right: 22px; top: 274px;
    text-align: center;
    font-size: 14px;
    letter-spacing: 3.4px;
    color: var(--slogan-grey);
  }
</style>
</head>
<body>
  <section class="card card--front">
    <div class="panel-pattern" role="img" aria-label="Faint geometric 3D wall panel pattern in white and light grey"></div>
    <div class="brand">
      <span class="brand__square"></span>
      <span class="brand__name">Orrin Linings</span>
    </div>
  </section>

  <section class="card card--back">
    <div class="contact-person">
      <p class="contact-person__name">Callum Brierley</p>
      <p>managing director</p>
      <p class="contact-person__mobile">M <b>04 1870 3362</b></p>
    </div>
    <div class="panel-pattern" role="img" aria-label="Faint geometric 3D wall panel pattern in white and light grey"></div>
    <div class="brand">
      <span class="brand__square"></span>
      <span class="brand__name">Orrin Linings</span>
    </div>
    <div class="contact-business">
      <p>P <b>02 9418 6030</b>&nbsp; F <b>02 9418 6031</b></p>
      <p>14 Calder Lane, Marrick Vale NSW 2190</p>
      <p>sales@orrinlinings.com.au</p>
      <p class="web">www.orrinlinings.com.au</p>
    </div>
    <p class="slogan">decorative panels for interiors &amp; exteriors</p>
  </section>
</body>
</html>
```